依頼詳細
第一回公演のチラシデザインを依頼したいです。

初回公演のタイトルは「日々硝子」

人は生きているだけで無数のドラマを生み出す。
それはその人に取っては重要で、他人にとっては些細な一面。
誰にもいうことはないけれど、自分の中で確かに起きる数々の感情の変化。
友情、恋愛、家族、夢。
何が人を作り、何が人を動かすのか。
誰かの長い人生のほんの一部を切り取り並べた『日々硝子』
あなたの中にもきっとある。
そんな感情のストーリー。

このようなテーマのダンス公演です。

■チラシのイメージは
<表面>
「水彩画」
「ステージで1本のスポットライトを浴びている女性」
「タイトル文字」

<裏面>
表面のイメージを採用しつつ、下記記載事項を掲載して下さい。

裏面→イベント名、日程、アクセス
チケット料金、問い合わせ先
出演者の名前、スタッフクレジット、SNSへのQRコード

デザインの雰囲気は暗めで、
記載項目
【フライヤーの記載内容詳細】
・記載事項
表面
イベントタイトル「日々硝子」

裏面

イベント名:Dance Company PEX第一回公演「日々硝子」

日程:2022年9月3日(土)・4日(日)

アクセス:会場「ヴェルナ・ホール」
https://verna-hall.example/access/

チケット料金:¥3,000

問い合わせ先:公式インスタグラムよりDM

出演:ぬい/朝比奈澄/宇野咲良/辻堂早苗/森永つばさ/浜口紗英/桑原理恵/堀ゆずは/綾瀬千尋/今井澪/葛西陽一郎/北条美奈子/戸部和泉/菅野拓真

スタッフクレジット
制作:矢島紬/根本彩花/江藤まどか
振付:菅野拓真/ぬい/朝比奈澄/宇野咲良/葛西陽一郎/北条美奈子
照明:株式会社ペルカ
音響:杉浦晃司

SNSへのQRコード→インスタグラムURLはこちら
https://www.instagram.com/dancecompanypex/?igshid=QxRtUwVb9Z=

主催:株式会社VEN
サイズ
A5
ページ数
両面
希望イメージ
シンプル 複雑
単色 カラフル
暗い 明るい
日常 高級
遊び心 厳粛
未来的 伝統的
女性的 男性的
希望する色
青系、無彩色系
納品ファイル
• 高解像度JPG (.jpg)
• イラストレーター形式 (.ai)
補足説明
※記載事項の詳細につきましては現状仮となっております。
※添付ファイルについて
フライヤー表面のイメージ画像を添付しておりますので、色味や質感、雰囲気を参考にしていただけたらと思います。
ご確認を宜しくお願い致します。
■ 選んだ理由

こちらのイメージをしっかりと組んだ水彩画でのデザインをご提案くださいました。

■ 提案者全員のお礼・コメント

この度はコンペにご参加頂きありがとうございました。
素敵なデザインをご提案くださり大変助かりました!!

```html
<!DOCTYPE html>
<html lang="ja">
<head>
<meta charset="UTF-8">
<title>Dance Company PEX 第一回公演「日々硝子」</title>
<link rel="stylesheet" href="https://fonts.googleapis.com/css2?family=Noto+Serif+JP:wght@500;700&family=Noto+Sans+JP:wght@500;700;900&family=Josefin+Sans:wght@400&display=swap">
<style>
  :root {
    --ink-light: #fbf6ef;
    --accent: #f3c27a;
    --olive: #6f6c4c;
    --moss: #5d6a48;
    --crimson: #9c3b2c;
    --wine: #6e2a31;
    --rose: #c36a5d;
    --stage-dark: #0b0b0d;
    --stage-light: #d9dde2;
    --line-pink: rgba(240, 190, 190, 0.55);
  }
  html, body {
    margin: 0;
    padding: 0;
    width: 847px;
    height: 1200px;
    overflow: hidden;
    background: #222;
  }
  .flyer {
    position: relative;
    width: 847px;
    height: 1200px;
    overflow: hidden;
    background:
      radial-gradient(circle at 15% 12%, rgba(140, 138, 96, 0.9) 0 22%, transparent 45%),
      radial-gradient(circle at 40% 55%, rgba(190, 70, 50, 0.85) 0 20%, transparent 45%),
      radial-gradient(circle at 85% 70%, rgba(110, 120, 70, 0.85) 0 18%, transparent 42%),
      radial-gradient(circle at 20% 85%, rgba(120, 40, 55, 0.9) 0 22%, transparent 50%),
      radial-gradient(circle at 70% 95%, rgba(150, 60, 55, 0.85) 0 20%, transparent 45%),
      linear-gradient(170deg, var(--olive) 0%, var(--crimson) 50%, var(--wine) 100%);
  }
  .watercolor-texture {
    position: absolute;
    inset: 0;
    opacity: 0.5;
    background:
      radial-gradient(circle at 30% 30%, rgba(200, 120, 90, 0.45) 0 12%, transparent 28%),
      radial-gradient(circle at 60% 40%, rgba(93, 106, 72, 0.5) 0 14%, transparent 30%),
      radial-gradient(circle at 50% 75%, rgba(195, 106, 93, 0.5) 0 15%, transparent 32%);
  }
  .stage-photo {
    position: absolute;
    left: 503px;
    top: 0;
    width: 344px;
    height: 607px;
    background:
      radial-gradient(ellipse 120px 300px at 52% 0%, rgba(217, 221, 226, 0.55), transparent 75%),
      radial-gradient(ellipse 160px 60px at 45% 92%, rgba(120, 120, 125, 0.35), transparent 80%),
      var(--stage-dark);
  }
  .cross-lines {
    position: absolute;
    inset: 0;
  }
  .company-line {
    position: absolute;
    left: 405px;
    top: 30px;
    writing-mode: vertical-rl;
    font-family: "Josefin Sans", "Noto Sans JP", sans-serif;
    font-size: 24px;
    letter-spacing: 0.42em;
    color: var(--ink-light);
    margin: 0;
    font-weight: 400;
  }
  .company-line .edition {
    font-family: "Noto Sans JP", sans-serif;
    font-weight: 500;
    letter-spacing: 0.15em;
  }
  .title {
    position: absolute;
    left: 330px;
    top: 570px;
    margin: 0;
    font-family: "Noto Serif JP", serif;
    font-weight: 500;
    color: var(--ink-light);
    line-height: 1;
  }
  .title span { display: block; }
  .title .first { font-size: 122px; letter-spacing: 0.08em; }
  .title .second { font-size: 112px; letter-spacing: 0.12em; margin: 24px 0 0 62px; }
  .event-info {
    position: absolute;
    left: 68px;
    top: 980px;
    font-family: "Noto Sans JP", sans-serif;
    color: var(--ink-light);
    font-weight: 700;
  }
  .event-info .year { font-size: 22px; color: var(--accent); margin: 0 0 2px 70px; }
  .event-info .year small { font-size: 13px; }
  .event-info .row { display: flex; align-items: baseline; margin: 0; }
  .event-info .label { font-size: 17px; font-weight: 500; margin-right: 10px; }
  .event-info .date { font-size: 40px; font-weight: 900; letter-spacing: 0.02em; }
  .event-info .date small { font-size: 26px; }
  .event-info .day {
    display: inline-block;
    font-size: 20px;
    width: 26px;
    height: 26px;
    line-height: 26px;
    text-align: center;
    border-radius: 50%;
    background: var(--ink-light);
    color: var(--wine);
    margin: 0 4px;
    vertical-align: 6px;
  }
  .event-info .venue { font-size: 22px; font-weight: 700; }
</style>
</head>
<body>
  <main class="flyer">
    <div class="watercolor-texture" role="img" aria-label="赤と緑の水彩の円が重なる背景"></div>

    <div class="stage-photo" role="img" aria-label="暗いステージで一本のスポットライトを浴びて立つ女性のシルエット"></div>

    <svg class="cross-lines" width="847" height="1200" viewBox="0 0 847 1200" aria-hidden="true">
      <g fill="var(--line-pink)">
        <rect x="328" y="470" width="10" height="360"/>
        <rect x="170" y="620" width="340" height="9"/>
        <rect x="508" y="680" width="10" height="520"/>
        <rect x="300" y="698" width="547" height="9"/>
        <rect x="75" y="280" width="7" height="420"/>
        <rect x="0" y="410" width="210" height="7"/>
      </g>
    </svg>

    <h2 class="company-line">Dance Company PEX <span class="edition">第一回公演</span></h2>

    <h1 class="title"><span class="first">日々</span><span class="second">硝子</span></h1>

    <section class="event-info">
      <p class="year">2022<small>年</small></p>
      <p class="row"><span class="label">日程：</span><span class="date">9<small>月</small>3<small>日</small></span><span class="day">土</span><span class="date">・4<small>日</small></span><span class="day">日</span></p>
      <p class="row"><span class="label">会場：</span><span class="venue">ヴェルナ・ホール</span></p>
    </section>
  </main>
</body>
</html>
```